Corporate speaking flyer for email

Redesign existing and very lame flyer. This is for my speaking business to be used as an introduction of content and style and my presentations. More photos can be provided. As you will see I'm an adventurer who makes part of my living from speaking about my adventures. The bio describes the general gist of that. There is more I could say but wanting to keep it pretty brief so as not to bore potential clients. Having said that I'd like to try and capture them in the first instance.

Target Market(s)

Corporate, clubs, events

Industry/Entity Type

Business

Requirements
Must have
• bio and references. Content provided. Feel free to edit.
Nice to have
• Surprise me!
Should not have
• Rude words.

```html
<!DOCTYPE html>
<html lang="en">
<head>
<meta charset="utf-8">
<title>Sam Calder – Motivational Speaker</title>
<link href="https://fonts.googleapis.com/css2?family=Oswald:wght@500;600&family=Roboto+Condensed:ital,wght@0,400;0,700;1,400&display=swap" rel="stylesheet">
<style>
:root{
  --navy:#1f3f63;
  --navy-dark:#19344f;
  --gold:#b2700f;
  --ink:#222;
  --rule:#b9894a;
  --paper:#fff;
  --backdrop:#ececec;
}
*{margin:0;padding:0;box-sizing:border-box}
html,body{width:1200px;height:1200px;overflow:hidden}
body{background:var(--backdrop);position:relative;font-family:"Roboto Condensed",Arial Narrow,sans-serif;color:var(--ink)}
.page{position:absolute;top:221px;width:537px;height:758px;background:var(--paper);box-shadow:0 1px 4px rgba(0,0,0,.18)}
.page--bio{left:45px}
.page--clients{left:620px}
.abs{position:absolute}
.photo{position:absolute;border:2px solid #fff}
/* bio page header */
.portrait{left:21px;top:21px;width:127px;height:140px;background:linear-gradient(135deg,#6b6a66,#3c3b39 60%,#2a2a2a)}
.header-bg{left:148px;top:21px;width:369px;height:96px;background:linear-gradient(90deg,#fff 30%,#efefef)}
.name{left:164px;top:26px;font-family:"Oswald",sans-serif;font-weight:600;font-size:28px;color:var(--gold);letter-spacing:.3px;line-height:1}
.role{left:164px;top:56px;font-size:17px;color:#222;line-height:1}
.tagline{left:164px;top:78px;font-size:24px;color:#111;line-height:1}
.tagline .q{color:var(--gold);font-family:"Oswald",sans-serif}
.contact-band{left:148px;top:117px;width:369px;height:45px;background:var(--navy)}
.contact{position:absolute;color:#dfe6ee;font-size:7.6px;line-height:11px;display:flex;align-items:center;gap:6px}
.contact svg{fill:#fff}
.bio{left:20px;top:177px;width:497px;font-size:7.3px;line-height:9.3px}
.bio p{margin-bottom:9.4px}
.band{left:0;width:537px;background:var(--navy)}
.band::after{content:"";position:absolute;left:0;right:0;bottom:-7px;height:7px;background:linear-gradient(#d8d8d8,#fff)}
.caption{position:absolute;left:0;right:0;bottom:0;height:13px;background:var(--gold);color:#fff;font-size:7.5px;line-height:13px;text-align:center}
.footer-url{left:0;width:537px;top:736px;text-align:center;font-size:9.5px;letter-spacing:1.8px;color:#333}
/* clients page */
.section-title{left:0;width:537px;top:18px;text-align:center;font-family:"Oswald",sans-serif;font-weight:600;font-size:22px;color:var(--gold);letter-spacing:.2px}
.col{position:absolute;top:57px;width:237px;height:456px;display:flex;flex-direction:column;justify-content:space-between}
.col--left{left:20px}
.col--right{left:279px}
.quote{font-size:6.95px;line-height:8.6px;text-align:justify}
.quote cite{display:block;text-align:right;font-style:italic;font-size:8px;margin-top:3px}
.rule{height:1px;background:var(--rule);margin:3px 0}
</style>
</head>
<body>

<section class="page page--bio">
  <div class="abs portrait" role="img" aria-label="Portrait of the speaker gesturing while talking"></div>
  <div class="abs header-bg"></div>
  <h1 class="abs name">SAM CALDER</h1>
  <div class="abs role">Motivational Speaker</div>
  <div class="abs tagline"><span class="q">“</span>Anything is Possible<span class="q">”</span></div>
  <div class="abs contact-band">
    <div class="contact" style="left:18px;top:13px">
      <svg width="12" height="12" viewBox="0 0 24 24"><path d="M6.6 10.8a15.1 15.1 0 0 0 6.6 6.6l2.2-2.2c.3-.3.7-.4 1-.2 1.1.4 2.3.6 3.6.6.6 0 1 .4 1 1V20c0 .6-.4 1-1 1A17 17 0 0 1 3 4c0-.6.4-1 1-1h3.5c.6 0 1 .4 1 1 0 1.3.2 2.5.6 3.6.1.3 0 .7-.2 1z"/></svg>
      <span>+64 (0)21 555 0142<br>+64 (0)7 555 0199</span>
    </div>
    <div class="contact" style="left:270px;top:13px">
      <span style="display:flex;flex-direction:column;gap:2px">
        <svg width="9" height="8" viewBox="0 0 24 20"><path d="M2 2h20v16H2z" fill="none" stroke="#fff" stroke-width="2.5"/><path d="M2 2l10 9 10-9" fill="none" stroke="#fff" stroke-width="2.5"/></svg>
        <svg width="9" height="9" viewBox="0 0 24 24"><circle cx="12" cy="12" r="10" fill="none" stroke="#fff" stroke-width="2.2"/><path d="M2 12h20M12 2c3 3 3 17 0 20M12 2c-3 3-3 17 0 20" fill="none" stroke="#fff" stroke-width="1.8"/></svg>
      </span>
      <span>sam@calderspeaks.co.nz<br>www.calderspeaks.com</span>
    </div>
  </div>

  <div class="abs bio">
    <p>Whether it’s laugh out loud humour, inspiration or thought provoking anecdotes and perspective, Sam Calder’s deeply moving presentations has it all.</p>
    <p>“An extraordinary mental and physical effort – something very, very special” is how Sir Graham Forde described Sam Calder and the late Tom Reeves’ incredible achievement in winning the inaugural Atlantic Rowing Race.</p>
    <p>Marathon rowing champion Sam Calder has been a New Zealand International rowing representative for 16 years. Sam’s numerous rowing achievements include World Champs silver, Commonwealth gold and a world record on the indoor rowing machine.</p>
    <p>Sam represented New Zealand at the Atlanta Olympics and published ‘The Open Rower’ on how he and Tom Reeves captured headlines around the world winning the grueling and inaugural Atlantic Rowing Race in 41 days. He then led teams to successful defenses in the next two editions making it a 3-peat of victories for New Zealand.</p>
    <p>He is co-organiser of the ‘Riverside 100’ (www.Riverside100.kiwi), ‘The Grand Regatta’ (www.TheGrandRegatta.co.nz), an annual rowing 8s clash between Northbank and visiting overseas universities on the Northbank River. His also recently conceived and managed a rowing expedition across the Tasman Sea.</p>
    <p>Ambitious goal-setting, teamwork and overcoming adversity in multiple Atlantic Rowing Race campaigns is the spine of Sam’s presentations, sandwiching the challenge of following his brother Daniel’s journey into Cambodia’s Khmer Rouge genocide www.BrotherStory.co.nz (optional topic). Powerful inspiring messages on tenacity, hope, love and the last human freedom: the power to choose your attitude and how you respond in a given situation. The humour, the insights and the emotional turning points have audiences spellbound.</p>
    <p>Sam will inspire you to pursue your dreams whatever they may be, to take on new challenges, overcoming hardship against the odds and know that with passion anything is possible!</p>
    <p>It doesn’t hurt to be just a little bit crazy too!</p>
    <p>Sam’s life is about following the dream, decision making, commitment, team building, goal setting, planning, focus, determination, positive thinking and, of course, winning!</p>
  </div>

  <div class="abs band" style="top:465px;height:264px">
    <div class="photo" style="left:20px;top:17px;width:150px;height:110px;background:linear-gradient(160deg,#d9952e,#7a5a34 45%,#3e5a78)" role="img" aria-label="Rower in a single scull on golden water"></div>
    <div class="photo" style="left:20px;top:138px;width:150px;height:110px;background:linear-gradient(180deg,#1f5fa8,#2c79c0 55%,#dfe7ee)" role="img" aria-label="Two rowers celebrating aboard the ocean rowing boat">
      <div class="caption">1997-The Atlantic Challenge</div>
    </div>
    <div class="photo" style="left:178px;top:17px;width:337px;height:231px;background:linear-gradient(170deg,#7fa3b6,#3f7aa0 35%,#6b6a55 65%,#9c6f4c)" role="img" aria-label="Two rowers cheering in their boat at the finish of the ocean race">
      <div class="caption">Tom Reeves and Sam Calder win the inaugural Atlantic Rowing Race</div>
    </div>
  </div>
  <div class="abs footer-url">www.calderspeaks.co.nz</div>
</section>

<section class="page page--clients">
  <h2 class="abs section-title">“WHAT CLIENTS ARE SAYING”</h2>

  <div class="col col--left">
    <div class="quote">“Sam has a remarkable story, told in a clever and compelling way. He is able to engage deeply with his audience; he made us laugh, cry and most importantly think deeply, as leaders, about our role in the world. One of the best!”<cite>Megan Hart, HR Manager, Dairyline</cite></div>
    <div class="rule"></div>
    <div class="quote">You are the second only speaker who made me cry and laugh and feel great all in one short time period, thank you so much for everything you do, and have done…..<cite>Lisa Morton, Harbour Rescue conference attendee</cite></div>
    <div class="rule"></div>
    <div class="quote">“Kids Care Trust was looking for an inspirational speaker who would reflect the passion, the hope and the commitment exhibited by KCT and its members. When I set out to look for such a person Sam Calder’s name kept bubbling to the surface and I’m delighted I made the phone call. Sam your speech is probably the most inspiring talk I have ever listened to. Your story is an amazing one delivered in a passionate and yet entertaining manner.”<cite>Ian Cole, CEO Southport Regional Airport</cite></div>
    <div class="rule"></div>
    <div class="quote">“… hearing your story was more inspirational than all the traditional “motivational” type trainers put together.”<cite>Mark Tilly, Tilly Realty</cite></div>
    <div class="rule"></div>
    <div class="quote">“The speaker was one of the most powerful I have listened to in years……incredible!”<cite>From client taken from conference feedback form</cite></div>
    <div class="rule"></div>
    <div class="quote">Sam was unbelievable, amazing, so well received, such a lovely guy, so humble. Had some of the audience in tears.<cite>Grant Weir, Harbourline Country Head</cite></div>
    <div class="rule"></div>
    <div class="quote">It was both an honour and a pleasure to be your host. The whole audience was captivated by your speech from start to finish. The clever way it was put together and how you incorporated our theme was fantastic. Your speech was truly inspirational and I personally have taken a lot out of it. The perspective on how I view challenges will change going forward as I am sure many others will too. I read a quote the other day that said ‘Don’t wait for sleep to dream’ and I think that sums it up nicely.<cite>Sandra Bell, Plainsview Regional Council</cite></div>
  </div>

  <div class="col col--right">
    <div class="quote">“One regular conference goer said I could organise another 50 conferences and not see a presentation as good as that.”<cite>Leonard Fraser, Petroline</cite></div>
    <div class="rule"></div>
    <div class="quote">We have received nothing but the highest praise for your open and honest talk – many people have been deeply moved by your story and it was the highlight of the sessions.<cite>Hannah Lowe, Harbourline EA to Country Head</cite></div>
    <div class="rule"></div>
    <div class="quote">“Listening to Sam speak is a breath of fresh air! Too often we come across heroes that seem untouchable, unattainable. But Sam’s earthy humour and humble nature coupled with an unwavering drive and determination gives his story palpable appeal and something that the everyday person can truly connect with. Communicating with a passion that is infectious, Sam’s story is one of triumph and tragedy and provides any listener the inspiration to get beyond the mindset of ‘just getting by’ when enduring tough or challenging times. He imparts the wisdom and notion that self- belief is critical and more importantly ‘possible’ for every one of us to achieve on our own personal journey to success.”<cite>Julia Evans, Faculty Management, Melbourne</cite></div>
    <div class="rule"></div>
    <div class="quote">Sam was outstanding. As requested he arrived early and set himself up with minimal assistance using our equipment. He was seated at the top table with some of our senior ranked officers and clearly struck a rapport early on, he skillfully (craftily) knitted some of this into the early part of his talk which was captivating and all were taken along on the roller coaster journey he portrays. He managed to lift the room initially before plummeting down into a deep and (not depressing) emotional low. This is done in such a way that he brings you along with him before raising your spirits once more and filling the room with laughter at the talks close.<br>Sam cleverly molded his message around his audience and expressed great respect for the military people in the room. This was appreciated.<br>I would highly recommend Sam to any audience.<cite>Capt Richard Barton, Defence Training Unit</cite></div>
    <div class="rule"></div>
    <div class="quote">“I thought that you would be outstanding concluding Conference but I could not have expected the performance that you delivered. It blew everyone away Sam and it got in touch with their humanity which is what I wanted Physical Educators to go back to and to discover the power within. Thanks so very much for providing a conclusion to Conference that was extraordinarily powerful with such an invaluable message for all present.”<cite>Graham Porter, Physical Educators Guild</cite></div>
  </div>

  <div class="abs band" style="top:526px;height:203px">
    <div class="photo" style="left:20px;top:14px;width:239px;height:175px;background:linear-gradient(180deg,#cfcfcf,#8a8a8a 55%,#3a3a3a)" role="img" aria-label="Black and white photo of the speaker presenting on stage to a seated audience"></div>
    <div class="photo" style="left:279px;top:14px;width:239px;height:175px;background:linear-gradient(150deg,#7d9a6a,#8b8178 45%,#c8b7a6)" role="img" aria-label="Speaker greeting an elderly man who holds flowers at an outdoor gathering"></div>
  </div>
  <div class="abs footer-url">www.calderspeaks.co.nz</div>
</section>

</body>
</html>
```